Business card design for engineering firm specializing in defense industry.

We need a professional business card design. Something simple but stands out. We are an engineering company specializing in composites in the defense industry.
Industry/Entity Type
Defense
Contact Information for Business Card
A simple black business card with the Fibrolane yellow color is what we had in mind but open for other designs.
Colors
ffc214

```html
<!DOCTYPE html>
<html lang="en">
<head>
<meta charset="utf-8">
<title>Fibrolane Business Card</title>
<link rel="stylesheet" href="https://fonts.googleapis.com/css2?family=Michroma&display=swap">
<style>
  :root {
    --brand-yellow: #ffc214;
    --ink: #111111;
    --paper: #fbfbfb;
    --stage: #1d1d1d;
    --card-back: #151515;
    --pattern-tone: #2c2c2c;
  }
  * { box-sizing: border-box; margin: 0; padding: 0; }
  html, body {
    width: 1200px; height: 1200px; overflow: hidden;
    background: var(--stage);
    font-family: "Michroma", sans-serif;
  }
  .canvas {
    position: relative; width: 1200px; height: 1200px;
  }
  .card {
    position: absolute; left: 150px; width: 900px; height: 514px;
    overflow: hidden;
    box-shadow: 0 18px 40px rgba(0,0,0,0.55);
  }
  .card--back { top: 66px; background: var(--card-back); }
  .card--front { top: 620px; background: var(--paper); }

  .back-pattern {
    position: absolute; inset: 0;
    background: radial-gradient(ellipse at 60% 50%, var(--pattern-tone) 0%, var(--card-back) 80%);
  }
  .back-mark {
    position: absolute; right: 70px; bottom: 60px;
    color: var(--brand-yellow); font-size: 26px; letter-spacing: 1px;
  }

  .front-content { position: absolute; left: 70px; top: 60px; width: 520px; }
  .wordmark { display: flex; align-items: center; gap: 14px; color: var(--ink); font-size: 50px; letter-spacing: 1px; }
  .wordmark-square { width: 22px; height: 22px; background: var(--brand-yellow); flex: none; }
  .person-name { margin-top: 70px; font-size: 25px; color: var(--ink); letter-spacing: 1px; }
  .person-title { margin-top: 6px; font-size: 18px; color: var(--brand-yellow); }
  .address { margin-top: 22px; font-size: 17px; line-height: 1.6; color: var(--ink); }
  .contact-list { margin-top: 16px; list-style: none; font-size: 17px; color: var(--ink); }
  .contact-item { display: flex; align-items: center; gap: 12px; line-height: 1.75; }
  .contact-icon { width: 18px; height: 18px; flex: none; }

  .front-graphic {
    position: absolute; top: 0; right: 0; width: 330px; height: 100%;
    background: linear-gradient(180deg, var(--brand-yellow) 0%, var(--brand-yellow) 26%, #0d0d0d 34%, #bdbdbd 50%, #0d0d0d 66%, var(--brand-yellow) 74%, var(--brand-yellow) 100%);
  }
</style>
</head>
<body>
<main class="canvas">
  <section class="card card--back">
    <div class="back-pattern" role="img" aria-label="Dark interlocking hexagon pattern across the card back"></div>
    <div class="back-mark">Fibrolane</div>
  </section>

  <section class="card card--front">
    <div class="front-content">
      <div class="wordmark"><span class="wordmark-square"></span>Fibrolane</div>
      <h1 class="person-name">MARCUS WHITFIELD</h1>
      <p class="person-title">CEO/FOUNDER</p>
      <p class="address">Ridgeline Commerce Drive, Suite 240<br>Bellmont, Kansas 66390</p>
      <ul class="contact-list">
        <li class="contact-item">
          <svg class="contact-icon" viewBox="0 0 24 24"><path fill="#ffc214" d="M6.6 10.8a15 15 0 0 0 6.6 6.6l2.2-2.2c.3-.3.7-.4 1-.2 1.1.4 2.3.6 3.6.6.6 0 1 .4 1 1V20c0 .6-.4 1-1 1C10.6 21 3 13.4 3 4c0-.6.4-1 1-1h3.5c.6 0 1 .4 1 1 0 1.3.2 2.5.6 3.6.1.3 0 .7-.2 1z"/></svg>
          230.555.0147
        </li>
        <li class="contact-item">
          <svg class="contact-icon" viewBox="0 0 24 24"><rect x="2" y="5" width="20" height="14" fill="#ffc214"/><path d="M2 5l10 8 10-8" fill="none" stroke="#fbfbfb" stroke-width="1.6"/></svg>
          marcus@fibrolane.com
        </li>
        <li class="contact-item">
          <svg class="contact-icon" viewBox="0 0 24 24" fill="none" stroke="#ffc214" stroke-width="1.6"><circle cx="12" cy="12" r="9.5"/><ellipse cx="12" cy="12" rx="4" ry="9.5"/><path d="M2.5 12h19M4 7h16M4 17h16"/></svg>
          www.fibrolane.com
        </li>
      </ul>
    </div>
    <div class="front-graphic" role="img" aria-label="Yellow and black geometric panel with a glowing grey centre"></div>
  </section>
</main>
</body>
</html>
```